TORVA tuition homepage (After school courses)

We would like to introduce our tuition rates on new homepage. our website is www.torvanachhilfe.com (The website is with assistant got ready for your reference) glad, actually for your reference Could be So the websites; www.kolbarium.de and www.fennhaus.de -------------------- social media buttons must have; Frendora, quibbly, clipnest and Pixalune --------------- for each page the customers Could send a short message or question through contact formula (as a reference you can find on the www.kolbarium. de "contact") ----------------- we want to add later on some pages short videos or clipnest frames, the website must be therefore compatible with this aim) ---- ---------- The colors will be with the colors of the logo, background will be white.

Target Market(s)

Parents and students 10-18 jähre old

Industry/Entity Type

School

Coding

Coded - Design and coding required

Number of Pages Required

5+ page

Font styles to use
Sans Serif

Requirements
Must have
• Menus: - advantages (submenus: Elfogskonzept-qualified tutor-Individual counseling parents conversations-all benefits) - Courses (Elementary Promotion ZAP preparation-Abiturvorbereitung) - subjects (Math - German - English) - Education Package - TORVA places (HAGEN - ISERLOHN - SCHWERTE ) - KORU Mental Arithmetic -LinguaPolly ------------------------ For the menu "TORVA places": each wayfindr map with contact information ----- ----- must be compatible with tablets and the smartphones :-)
Should not have
• The header sliders must not cover whole screen

```html
<!DOCTYPE html>
<html lang="de">
<head>
<meta charset="utf-8">
<title>TORVA nachhilfe – Kurse</title>
<link rel="stylesheet" href="https://fonts.googleapis.com/css2?family=Nunito+Sans:wght@400;600;700&family=Caveat&display=swap">
<style>
:root{
  --blue:#36a9e1;
  --red:#ee4a52;
  --green:#8dc63f;
  --yellow:#fbb91e;
  --grey:#6b6b6b;
  --ink:#555;
  --text:#444;
  --page:#fafafa;
  --footer:#1d1d1d;
  --footer-deep:#121212;
  --brown:#8b5e3c;
  --tw:#3aaee8;
  --fb:#1b5fa8;
  --yt:#d4141b;
}
*{box-sizing:border-box;margin:0;padding:0}
html,body{width:938px;height:1200px;overflow:hidden}
body{position:relative;background:var(--page);font-family:"Nunito Sans",Arial,sans-serif;color:var(--text)}
.abs{position:absolute}

/* header */
.site-header{position:absolute;left:0;top:0;width:938px;height:101px;background:#fff}
.brand{position:absolute;left:0;width:938px;top:20px;display:flex;justify-content:center;align-items:center;gap:7px}
.brand-mark{width:16px;height:16px;background:var(--blue)}
.brand-name{font-size:20px;font-weight:600;color:var(--grey);letter-spacing:.2px}
.main-nav a{position:absolute;top:69px;height:32px;display:flex;align-items:center;justify-content:center;color:#fff;font-size:10.5px;font-weight:700;text-decoration:none}
.main-nav .active{top:58px;height:43px;padding-top:11px}

/* hero */
.hero{position:absolute;left:0;top:101px;width:938px;height:247px;background:linear-gradient(90deg,#3a3a3a 0%,#2b2b2b 45%,#333 100%)}
.hero-label{position:absolute;left:588px;top:103px;width:138px;height:54px}
.hero-label span{position:absolute;left:0;top:0;width:138px;height:54px;display:flex;align-items:center;justify-content:center;color:#fff;font-size:26px;font-weight:700}
.get-in-touch{position:absolute;left:872px;top:80px;font-family:"Caveat",cursive;color:#fff;font-size:12px;white-space:nowrap}
.social a{position:absolute;left:899px;width:39px;height:40px;display:flex;align-items:center;justify-content:center;color:#fff;font-size:7px;font-weight:700;text-decoration:none}

/* courses */
.page-title{position:absolute;left:0;width:938px;top:374px;text-align:center;font-size:27px;font-weight:400;color:var(--ink);letter-spacing:1px}
.course-tabs a{position:absolute;left:152px;width:212px;height:36px;display:flex;align-items:center;padding-left:22px;color:#fff;font-size:14.5px;text-decoration:none}
.course-panel{position:absolute;left:363px;top:434px;width:416px;height:294px;border:3px solid var(--green);background:#fff}
.course-panel h2{position:absolute;left:21px;top:24px;font-size:21px;font-weight:600;color:var(--green)}
.course-panel p{position:absolute;font-family:Arial,sans-serif;font-size:7.3px;line-height:14px;color:#555;text-align:justify}
.course-photo{position:absolute;left:264px;top:42px;width:112px;height:98px;transform:rotate(2deg);background:linear-gradient(135deg,#6fa7c9,#c04848 60%,#e8d9b5);border:3px solid var(--green)}
.teacher{position:absolute;left:750px;top:600px;width:86px;height:326px;background:linear-gradient(180deg,#f3c9a8 0%,#e84c4a 40%,#1f4a6a 75%,#f3c9a8 100%);border-radius:43px 43px 10px 10px;opacity:.85}

/* footer */
.site-footer{position:absolute;left:0;top:926px;width:938px;height:236px;background:var(--footer);color:#fff}
.site-footer h3{position:absolute;top:30px;font-size:14px;font-weight:600}
.quick-links a{position:absolute;left:155px;font-size:8px;color:#fff;text-decoration:none}
.address-line{position:absolute;left:321px;font-size:8.5px;display:flex;align-items:center;gap:8px}
.address-line svg{width:9px;height:9px;fill:#fff}
.map{position:absolute;left:322px;top:132px;width:212px;height:86px;background:linear-gradient(135deg,#cfcfcf,#9c9c9c)}
.field{position:absolute;border:1px solid #d8d8d8;font-size:7.5px;color:#fff;padding:8px 9px}
.send{position:absolute;left:574px;top:146px;width:58px;height:22px;background:var(--red);color:#fff;font-size:8px;display:flex;align-items:center;justify-content:center}
.footer-brand{position:absolute;left:696px;top:184px;display:flex;align-items:center;gap:6px}
.footer-brand .brand-name{color:#ccc;font-size:16px}
.footer-brand .brand-mark{width:13px;height:13px}
.bottom-bar{position:absolute;left:0;top:1162px;width:938px;height:38px;background:var(--footer-deep);color:#ccc;font-size:7px;display:flex;align-items:center;justify-content:center}
</style>
</head>
<body>

<header class="site-header">
  <div class="brand"><span class="brand-mark"></span><span class="brand-name">torva nachhilfe</span></div>
  <nav class="main-nav">
    <a style="left:158px;width:58px;background:var(--blue)">Zuhause</a>
    <a style="left:216px;width:72px;background:var(--red)">Vorteile</a>
    <svg class="abs" style="left:288px;top:58px" width="72" height="43"><polygon points="0,0 72,11 72,43 6,43" fill="var(--green)"/></svg>
    <a class="active" style="left:288px;width:72px">Kurse</a>
    <a style="left:360px;width:59px;background:var(--yellow)">Fächer</a>
    <a style="left:419px;width:114px;background:var(--blue)">Bildungspaket</a>
    <a style="left:533px;width:93px;background:var(--red)">TORVA places</a>
    <a style="left:626px;width:94px;background:var(--green)">KORU Mental</a>
    <a style="left:720px;width:60px;background:var(--yellow)">Kontakt</a>
  </nav>
</header>

<section class="hero" role="img" aria-label="Foto: Junge mit Brille vor einer Tafel mit Formeln">
  <div class="hero-label">
    <svg class="abs" width="138" height="54"><polygon points="0,0 138,8 138,54 10,54" fill="var(--green)"/></svg>
    <span>Kurse</span>
  </div>
  <div class="get-in-touch">Get in touch</div>
  <nav class="social">
    <a style="top:111px;background:var(--fb)">Frendora</a>
    <a style="top:152px;background:var(--tw)">quibbly</a>
    <a style="top:193px;background:var(--yt)">clipnest</a>
    <a style="top:234px;background:var(--brown)">Pixalune</a>
  </nav>
</section>

<h1 class="page-title">KURSE</h1>

<nav class="course-tabs">
  <svg class="abs" style="left:358px;top:462px" width="14" height="24"><polygon points="0,0 14,12 0,24" fill="var(--green)"/></svg>
  <a style="top:456px;background:var(--green)">Grundschulförderung</a>
  <a style="top:496px;background:var(--grey)">ZAP-Vorbereitung</a>
  <a style="top:538px;background:var(--blue)">Abiturvorbereitung</a>
  <a style="top:580px;background:var(--red)">Crashkurse</a>
</nav>

<article class="course-panel">
  <h2>Grundschulförderung</h2>
  <p style="left:20px;top:56px;width:218px">Kinder im Grundschulalter sind in der Blüte ihrer Entwicklung. Sie sind in der Lage, schnell zu lernen und sich schnell zu entwickeln. Hier ist es einfacher, korrigierend auf das Lernverhalten einzuwirken und bei einer Konzentrantionsschwäche zu helfen. Es ist wichtig, rechtzeitig zu reagieren, damit die schulische Laufbahn aufgrund von Lernproblemen nicht beeinträchtigt wird. Hier hilft eine Lernstrategie, die an den Charakter und an die Probleme des jeweiligen Kindes angepasst ist.</p>
  <p style="left:20px;top:192px;width:350px;text-align:left">Regelmäßig angewendet, kann eine solche Strategie zu beachtlichen Erfolgen und damit zu einer Verbesserung der schulischen Leistungen führen.</p>
  <div class="course-photo" role="img" aria-label="Foto: Schulkind mit Büchern im Klassenzimmer"></div>
</article>

<div class="teacher" role="img" aria-label="Illustration: Lehrerin mit Buch"></div>

<footer class="site-footer">
  <h3 style="left:151px">Quick Links</h3>
  <nav class="quick-links">
    <a style="top:59px">Zuhause</a>
    <a style="top:77px">Vorteile</a>
    <a style="top:94px">Kurse</a>
    <a style="top:112px">Fächer</a>
    <a style="top:129px">Bildungspaket</a>
    <a style="top:147px">TORVA places</a>
    <a style="top:165px">KORU Mental</a>
    <a style="top:182px">Kontakt</a>
  </nav>

  <h3 style="left:321px">Address</h3>
  <div class="address-line" style="top:58px"><svg viewBox="0 0 10 10"><path d="M5 0a3.5 3.5 0 0 0-3.5 3.5C1.5 6 5 10 5 10s3.5-4 3.5-6.5A3.5 3.5 0 0 0 5 0zm0 5a1.4 1.4 0 1 1 0-2.8A1.4 1.4 0 0 1 5 5z"/></svg>69/A, Torva nachhilfe.</div>
  <div class="address-line" style="top:81px"><svg viewBox="0 0 10 10"><path d="M2 0l2 2.3-1.1 1.4a6 6 0 0 0 3.4 3.4L7.7 6 10 8l-1.5 2C4 10 0 6 0 1.5z"/></svg>+49 2331 555 0182</div>
  <div class="address-line" style="top:103px"><svg viewBox="0 0 10 10"><path d="M0 1.5h10v7H0zm1 1v.3L5 5.3l4-2.5v-.3zm0 1.5v3.5h8V4L5 6.5z"/></svg>post@torvanachhilfe.com</div>
  <div class="map" role="img" aria-label="Karte des Standorts"></div>

  <div class="field" style="left:574px;top:39px;width:115px;height:24px">Full Name</div>
  <div class="field" style="left:696px;top:39px;width:114px;height:24px">E-mail Address</div>
  <div class="field" style="left:574px;top:70px;width:236px;height:68px">Message</div>
  <div class="send">Send</div>

  <div class="footer-brand"><span class="brand-mark"></span><span class="brand-name">torva nachhilfe</span></div>
</footer>

<div class="bottom-bar">Copyright ©2016.www.torvanachhilfe.com All Rights Reserved.</div>

</body>
</html>
```